Optometry office needs a postcard to get name out to local schools

I need a postcard design for an optometry office called "Hosaru Optometry".
I want to get our name out to local schools and with this short letter and advertisement.
I want to keep the baby blue /navy blue colors theme.
One the front i want the following
Front:
1) three lines for the address of the recipient as in the example, and square for the postage in the upper right hand corner.
2) our logo with "Hosaru Optometry" and a horizontal line with our website address just below the line as in the example.
put the words "Our practice is committed to supporting our community and local schools." and our phone number "714-390-5264"
3) perhaps more contact info is looks neat and not too cluttered
Back:
1) letter which is attached
2) maybe a small clip art like a phoropter or glasses or something eye related

```html
<!DOCTYPE html>
<html lang="en">
<head>
<meta charset="utf-8">
<title>Hosaru Optometry – Letter to Schools</title>
<link href="https://fonts.googleapis.com/css2?family=Carlito:ital@0;1&family=Arimo&display=swap" rel="stylesheet">
<style>
  :root {
    --teal: #2cb3a0;
    --letter-blue: #2f6db5;
    --paper: #ffffff;
    --device-light: #c9ccd0;
    --device-dark: #3a3d42;
  }
  html, body {
    margin: 0;
    padding: 0;
    overflow: hidden;
    background: var(--paper);
  }
  .postcard {
    position: relative;
    width: 1200px;
    height: 867px;
    background: var(--paper);
    overflow: hidden;
  }
  .office-block {
    position: absolute;
    left: 43px;
    top: 50px;
    margin: 0;
    font-family: "Carlito", "Calibri", sans-serif;
    font-style: normal;
    font-size: 22px;
    line-height: 36.5px;
    color: var(--teal);
  }
  .online-block {
    position: absolute;
    right: 38px;
    top: 44px;
    margin: 0;
    text-align: right;
    font-family: "Carlito", "Calibri", sans-serif;
    font-style: italic;
    font-size: 22px;
    line-height: 36px;
    color: var(--teal);
  }
  .letter {
    position: absolute;
    left: 43px;
    top: 0;
    width: 1140px;
    font-family: "Arimo", "Arial", sans-serif;
    font-size: 19.4px;
    line-height: 27.8px;
    color: var(--letter-blue);
  }
  .letter p {
    position: absolute;
    left: 0;
    width: 1140px;
    margin: 0;
  }
  .salutation { top: 219px; }
  .intro { top: 275px; }
  .mission { top: 358px; }
  .referrals { top: 496px; }
  .closing { top: 607px; }
  .sign-off { top: 663px; }
  .signature {
    position: absolute;
    left: 40px;
    top: 724px;
    margin: 0;
    font-family: "Carlito", "Calibri", sans-serif;
    font-size: 34px;
    color: var(--teal);
  }
  .phoropter-art {
    position: absolute;
    left: 939px;
    top: 615px;
    width: 213px;
    height: 203px;
    border-radius: 40px 40px 60px 60px;
    background: radial-gradient(circle at 50% 55%, var(--device-light) 0%, #8d9197 45%, var(--device-dark) 100%);
  }
</style>
</head>
<body>
  <main class="postcard">
    <address class="office-block">
      Hosaru Optometry<br>
      4120 Orchard Grove Ave Ste B<br>
      Maple Hills, CA 90418<br>
      714-390-5264
    </address>

    <address class="online-block">
      hosaruoptometry@mailbox.com<br>
      www.hosaruoptometry.com
    </address>

    <article class="letter">
      <p class="salutation">Dear</p>
      <p class="intro">I would like to introduce our family optometry office that has been in business for the past 35 years! We are located at 4120 Orchard Grove Ave Ste B in Maple Hills (near Orchard Grove Ave and Cedar Blvd).</p>
      <p class="mission">Our practice is committed to supporting our community and local schools by taking care of adults and children of all ages. As 80% of learning is done visually, it is especially important for young children to have access to routine comprehensive eye care. Our goal is to provide excellent eye care for the families as well as quality ophtalmic frames and lenses at reasonable prices.</p>
      <p class="referrals">We are happy to see any referrals from you, including students who have not passed vision screenings or have other ocular health concerns. Please feel free to reach out to us if you have any questions. You can contact us by phone or email, and are also welcome to visi our office anytime.</p>
      <p class="closing">We look forward to a strong relationship together and success for all your students.</p>
      <p class="sign-off">Sincerely,</p>
    </article>

    <p class="signature">Kenji Hosaru, OD</p>

    <div class="phoropter-art" role="img" aria-label="Illustration of a phoropter eye-testing instrument"></div>
  </main>
</body>
</html>
```